Lumora Studio Opening Flyer (German Text Involved!)

We need a double-sided flyer design for a new beauty studio in Zurich, Switzerland called "Lumora Studio" our services are Laser Hair Removal, Diode Laser, Manicure, Pedicure, Massage, Makeup, Facial, and Waxing. Our main service is Laser Hair Removal. We would like to see designs that use the colors purple and white. The final design should communicate beauty for men and women. You will find the Logo in the attachments.

The flyer must be 105mm wide x 210mm tall.

The following text must be on the flyer:

FRONT TEXT:
Unser “Lumora Studio“ Studio liegt beim Bahnhof Murtelried. Wir sind dein Partner für natürliche Schönheit, ob Haut, Nägel, Wimpern oder Haarentfernungen. Wir verschönern dein Aussehen mit professionellen Behandlungen.

Eröffnungsrabatt von 20% für Neukunden bis Ende November 2020 auf Diodenlaser-Behandlungen.

Wir freuen uns auf deinen Besuch.

Lumora Studio, Erlenweg 27, 8600 Dübendorf, Tel. 044 713 29 84

www.lumora-studio.ch

BACK TEXT:
DIENSTLEISTUNGEN

Pediküre:
Auch Füsse brauchen Pflege. Die Pediküre mit erfrischendem Bad und kosmetischer Pflege zaubert Füsse, die sich sehen lassen können.

Maniküre:
Gepflegte Hände sind nicht nur unsere Visitenkarte, sie geben uns auch den ganzen Tag ein gutes Gefühl.

Haarentfernung:
Als attraktiv und ästhetisch gelten nicht nur eine gute Figur, sondern auch eine glatte, unbehaarte Haut, speziell für Frauen, aber zunehmend auch für Männer.

Wimpern-Lifting:
Voluminöse Wimpern geben den Augen Ausdrucksstärke und wirken verführerisch. Mit einem professionellen Wimpern-Lifting wird dieser Effekt noch verstärkt.

Maniküre, schon ab CHF 45.-
Pediküre, schon ab CHF 60.-
Dauerhafte Haarentfernung mit dem Diodenlaser, schon ab CHF 25.-
Haarentfernung mit Wachs, schon ab CHF 15.-

UNSERE ÖFFNUNGSZEITEN
Montag bis Samstag
09:00 bis 18:00

www.lumora-studio.ch

beauty for men and women

Beauty Salon

876aae

• FRONT TEXT:

www.lumora-studio.ch

BACK TEXT:
DIENSTLEISTUNGEN

Pediküre:

Maniküre:

Haarentfernung:

Wimpern-Lifting:

UNSERE ÖFFNUNGSZEITEN
Montag bis Samstag
09:00 bis 18:00

www.lumora-studio.ch

```html
<!DOCTYPE html>
<html lang="de">
<head>
<meta charset="utf-8">
<title>Lumora Studio – Dienstleistungen</title>
<link rel="stylesheet" href="https://fonts.googleapis.com/css2?family=Quicksand:wght@300;400&family=Ubuntu:wght@500&display=swap">
<style>
  :root {
    --purple-top: #8766ab;
    --purple-deep: #7350a5;
    --purple-mid: #8466ae;
    --purple-low: #6d4b9b;
    --lilac: #c596fa;
    --lilac-soft: #c2a6e0;
    --pink: #ff8ef0;
    --white: #ffffff;
    --ink: #5b3b94;
  }
  html, body {
    margin: 0;
    padding: 0;
    width: 1200px;
    height: 2400px;
    overflow: hidden;
    background: var(--white);
  }
  .flyer {
    position: relative;
    width: 1200px;
    height: 2400px;
    overflow: hidden;
    font-family: "Quicksand", sans-serif;
    font-weight: 300;
    font-style: normal;
    text-align: center;
  }
  .backdrop {
    position: absolute;
    inset: 0;
  }
  .brand-name {
    position: absolute;
    top: 92px;
    right: 40px;
    margin: 0;
    font-weight: 400;
    font-size: 32px;
    color: var(--lilac-soft);
  }
  .block {
    position: absolute;
    left: 0;
    width: 1200px;
    margin: 0;
    font-style: normal;
  }
  .page-title {
    top: 330px;
    font-family: "Ubuntu", sans-serif;
    font-weight: 500;
    font-size: 72px;
    line-height: 76px;
    color: var(--pink);
    letter-spacing: 1px;
  }
  .service h2 {
    margin: 0;
    font-weight: 300;
    font-size: 60px;
    line-height: 60px;
    color: var(--pink);
  }
  .service p,
  .prices p {
    margin: 0;
    font-size: 46px;
    line-height: 56px;
    color: var(--white);
  }
  .service--pedicure { top: 441px; }
  .service--manicure { top: 723px; }
  .service--hair { top: 1005px; }
  .service--lashes { top: 1288px; }
  .prices { top: 1627px; }
  .hours {
    top: 1961px;
    font-size: 46px;
    line-height: 56px;
    color: var(--pink);
  }
  .hours p { margin: 0; }
  .contact {
    top: 2160px;
    font-size: 48px;
    line-height: 56px;
    color: var(--ink);
  }
  .contact p { margin: 0; }
  .website {
    top: 2296px;
    font-size: 44px;
    line-height: 50px;
    color: var(--ink);
  }
</style>
</head>
<body>
<main class="flyer">
  <svg class="backdrop" viewBox="0 0 1200 2400" width="1200" height="2400" aria-hidden="true">
    <defs>
      <linearGradient id="panelShade" x1="0" y1="0" x2="0.3" y2="1">
        <stop offset="0" stop-color="#7350a5"/>
        <stop offset="0.5" stop-color="#8466ae"/>
        <stop offset="1" stop-color="#6d4b9b"/>
      </linearGradient>
    </defs>
    <rect x="0" y="0" width="1200" height="460" fill="var(--purple-top)"/>
    <path class="swoosh-white" d="M0,85 C320,-10 720,40 1200,345 L1200,430 C820,250 320,150 0,300 Z" fill="var(--white)"/>
    <path class="swoosh-lilac" d="M0,140 C300,55 610,85 835,235 C600,125 300,125 0,235 Z" fill="var(--lilac)"/>
    <path class="panel" d="M0,300 C300,150 720,175 1200,425 L1200,2057 C960,2060 820,2154 600,2154 C360,2154 230,2062 0,2067 Z" fill="url(#panelShade)"/>
  </svg>

  <p class="brand-name">Lumora Studio</p>

  <h1 class="block page-title">DIENSTLEISTUNGEN</h1>

  <section class="block service service--pedicure">
    <h2>Pediküre:</h2>
    <p>Auch Füsse brauchen Pflege. Die Pediküre mit<br>erfrischendem Bad und kosmetischer Pflege<br>zaubert Füsse, die sich sehen lassen können.</p>
  </section>

  <section class="block service service--manicure">
    <h2>Maniküre:</h2>
    <p>Gepflegte Hände sind nicht nur unsere<br>Visitenkarte, sie geben uns auch den ganzen Tag<br>ein gutes Gefühl.</p>
  </section>

  <section class="block service service--hair">
    <h2>Haarentfernung:</h2>
    <p>Als attraktiv und ästhetisch gelten eine gute<br>Figur und, speziell für Frauen, aber zunehmend<br>auch für Männer, eine glatte, unbehaarte Haut.</p>
  </section>

  <section class="block service service--lashes">
    <h2>Wimpern-Lifting:</h2>
    <p>Voluminöse Wimpern geben den Augen<br>Ausdrucksstärke und wirken verführerisch. Mit einem<br>professionellen Wimpern-Lifting wird dieser<br>Effekt noch verstärkt.</p>
  </section>

  <section class="block prices">
    <p>Maniküre, schon ab CHF 45.-<br>Pediküre, schon ab CHF 60.-<br>Dauerhafte Haarentfernung mit dem Diodenlaser,<br>schon ab CHF 25.-<br>Haarentfernung mit Wachs, schon ab CHF 15.-</p>
  </section>

  <section class="block hours">
    <p>UNSERE ÖFFNUNGSZEITEN</p>
    <p>Montag bis Samstag</p>
    <p>09:00 bis 18:00</p>
  </section>

  <address class="block contact">
    <p>Lumora Studio, Erlenweg 27, 8600 Dübendorf,</p>
    <p>Tel. 044 713 29 84</p>
  </address>

  <p class="block website">www.lumora-studio.ch</p>
</main>
</body>
</html>
```